Yard Nest+ - Outdoors Home Improvents, Upkeeing and Maintenance services

I need a website that looks environmental and refreshing. Yard Nest+ is a home upkeeping services and maintenance for all seasons. I will need a website that can create the feel or atmosphere of each season in separate tabs (ie for summer design should illustrate lawn mowing and gardening services etc while the winter would illustrate snow shovelling services likewise for fall illustratating leaves raking services. Each service should have there own feel to it as if the pages/tab was solely dedicated to that service. Four services in total winter, fall, spring, summer and would like it to have a fun and engaging feel to it with rollover images and links to service description pages.
Updates

Sorry name of the company is maple ridge can you revise the name. I will add a picture to the brief you can get the logo from Added Thursday, April 14, 2016

Target Market(s)

Home Owners, rental suites, landlords, real estate commercial/residential

Industry/Entity Type

Home Improvement

Number of Pages Required

4 page

Font styles to use
Serif
Decorative
Script

Colors
33b8a4
add136
fbee3d
ffffff
ec1f27
ffc214
f37122
f78f20
1b1b1b

Requirements
Must have
• Each service should have there own feel to it as if the pages/tab was solely dedicated to that service. Four services in total winter, fall, spring, summer and would like it to have a fun and engaging feel to it with rollover images and links to service description pages.
Nice to have
Should not have
• Dull and unwelcoming

```html
<!DOCTYPE html>
<html lang="en">
<head>
<meta charset="utf-8">
<title>Maple Ridge – Seasonal Home Upkeep</title>
<link href="https://fonts.googleapis.com/css2?family=Cinzel:wght@400;700&family=Open+Sans:ital,wght@0,400;0,600;1,400;1,700&display=swap" rel="stylesheet">
<style>
:root{
  --red:#ec1f27;
  --red-dark:#c9161d;
  --ink:#1b1b1b;
  --text:#444444;
  --white:#ffffff;
  --footer:#3a3a3a;
  --footer-bar:#2b2b2b;
  --footer-text:#e6e6e6;
  --moss:#5b6b3a;
}
*{margin:0;padding:0;box-sizing:border-box}
html,body{width:1200px;height:2287px;overflow:hidden}
body{position:relative;background:var(--white);font-family:"Open Sans",Arial,sans-serif;color:var(--text)}
.abs{position:absolute}

/* header */
.top-rule{left:0;top:0;width:1200px;height:3px;background:var(--red)}
.brand{left:92px;top:34px;width:150px;text-align:center}
.brand-dot{display:block;margin:0 auto 8px;width:52px;height:52px;border-radius:50%;background:var(--moss)}
.brand-name{font-family:"Cinzel",Georgia,serif;font-size:19px;color:var(--ink);letter-spacing:.5px;white-space:nowrap}
.header-phone{left:936px;top:40px;font-family:"Cinzel",Georgia,serif;font-size:21px;color:var(--ink);display:flex;align-items:center;gap:8px}
.main-nav a{position:absolute;top:92px;font-family:"Cinzel",Georgia,serif;font-size:15px;color:var(--ink);text-decoration:none;white-space:nowrap}
.main-nav a.is-active{color:var(--red)}
.nav-underline{left:466px;top:114px;width:68px;height:6px}

/* hero */
.hero{left:0;top:136px;width:1200px;height:512px;
  background:
    radial-gradient(ellipse 240px 260px at 1050px 110px,rgba(196,42,28,.95) 0%,rgba(196,42,28,0) 100%),
    radial-gradient(ellipse 170px 200px at 1170px 260px,rgba(214,70,30,.85) 0%,rgba(214,70,30,0) 100%),
    radial-gradient(ellipse 200px 240px at 300px 90px,rgba(214,170,60,.9) 0%,rgba(214,170,60,0) 100%),
    radial-gradient(ellipse 140px 200px at 60px 150px,rgba(120,150,60,.9) 0%,rgba(120,150,60,0) 100%),
    radial-gradient(ellipse 260px 160px at 560px 110px,rgba(150,150,150,.9) 0%,rgba(150,150,150,0) 100%),
    radial-gradient(ellipse 170px 150px at 650px 300px,rgba(70,60,55,.85) 0%,rgba(70,60,55,0) 100%),
    radial-gradient(ellipse 300px 120px at 170px 440px,rgba(60,90,45,.95) 0%,rgba(60,90,45,0) 100%),
    linear-gradient(180deg,#9a988f 0%,#8a8578 35%,#5e6a3a 62%,#6f5a35 82%,#8a6a3e 100%)}
.hero-shade{left:0;top:136px;width:1200px;height:512px;background:linear-gradient(90deg,rgba(0,0,0,.25) 0%,rgba(0,0,0,0) 55%)}
.hero-kicker{left:99px;top:366px;font-family:"Cinzel",Georgia,serif;font-size:20px;color:var(--white);letter-spacing:.5px}
.hero-title{left:99px;top:390px;font-family:"Cinzel",Georgia,serif;font-weight:700;font-size:34px;color:var(--white);letter-spacing:.5px}
.btn{display:flex;align-items:center;justify-content:center;background:var(--red);color:var(--white);font-size:13px;border-radius:3px;box-shadow:0 2px 0 var(--red-dark)}
.hero-btn{left:99px;top:444px;width:122px;height:41px}
.hero-arrow{top:395px}

.appointment{left:823px;top:204px;width:278px;height:409px;background:rgba(40,40,40,.88)}
.appointment-head{left:823px;top:204px;width:278px;height:40px;background:var(--red);color:var(--white);font-family:"Cinzel",Georgia,serif;font-size:17px;display:flex;align-items:center;justify-content:center}
.field{left:839px;width:248px;height:38px;border:1px solid rgba(255,255,255,.55);border-radius:3px;color:var(--white);font-size:12px;padding:10px}
.field-select{display:flex;justify-content:space-between;align-items:center;padding:0 12px 0 10px}
.field-area{height:76px}
.send-btn{left:839px;top:557px;width:110px;height:38px}

/* welcome */
.video-frame{left:99px;top:688px;width:400px;height:238px;border:4px solid var(--white);box-shadow:0 0 0 1px #ccc;
  background:
    radial-gradient(ellipse 90px 110px at 250px 90px,rgba(200,190,170,.9) 0%,rgba(200,190,170,0) 100%),
    radial-gradient(ellipse 120px 80px at 330px 60px,rgba(170,165,150,.9) 0%,rgba(170,165,150,0) 100%),
    radial-gradient(ellipse 90px 120px at 40px 100px,rgba(90,120,60,.95) 0%,rgba(90,120,60,0) 100%),
    radial-gradient(ellipse 200px 70px at 220px 210px,rgba(150,95,55,.95) 0%,rgba(150,95,55,0) 100%),
    radial-gradient(ellipse 80px 60px at 340px 160px,rgba(110,150,70,.9) 0%,rgba(110,150,70,0) 100%),
    linear-gradient(180deg,#d8d2c0 0%,#a99a7c 50%,#8a6a48 100%)}
.play{left:274px;top:787px;width:50px;height:38px;background:var(--red);border-radius:6px}
.section-title{font-family:"Cinzel",Georgia,serif;font-weight:400;font-size:32px;color:var(--ink);display:flex;align-items:center;gap:8px;white-space:nowrap}
.title-dot{width:44px;height:44px;border-radius:50%;background:var(--moss);flex:none}
.welcome-title{left:526px;top:698px}
.welcome-copy{left:523px;top:754px;width:578px;font-size:12px;line-height:24px;color:var(--text);text-align:justify}
.welcome-btn{left:523px;top:885px;width:143px;height:44px}

/* services */
.services{left:0;top:987px;width:1200px;height:573px;
  background:
    radial-gradient(ellipse 260px 300px at 80px 120px,rgba(170,175,165,.55) 0%,rgba(170,175,165,0) 100%),
    radial-gradient(ellipse 300px 260px at 1100px 420px,rgba(210,170,130,.5) 0%,rgba(210,170,130,0) 100%),
    linear-gradient(180deg,#ece8e4 0%,#f1ece7 50%,#ebe2d9 100%)}
.services-title{left:0;top:1028px;width:1200px;justify-content:center}
.season-tab{top:1101px;height:35px;font-size:12px;display:flex;align-items:center;justify-content:center;background:#f5f5f5;border:1px solid #ccc;color:var(--ink)}
.season-tab.is-active{background:var(--red);border-color:var(--red);color:var(--white)}
.service-card{top:1147px;width:239px;height:363px;background:var(--white);box-shadow:0 1px 3px rgba(0,0,0,.15)}
.service-photo{position:absolute;left:0;top:0;width:239px;height:180px}
.photo-sweep{background:
  radial-gradient(ellipse 70px 40px at 70px 110px,rgba(200,140,50,.95) 0%,rgba(200,140,50,0) 100%),
  radial-gradient(ellipse 90px 50px at 170px 150px,rgba(180,110,45,.9) 0%,rgba(180,110,45,0) 100%),
  radial-gradient(ellipse 60px 40px at 190px 60px,rgba(190,130,60,.85) 0%,rgba(190,130,60,0) 100%),
  linear-gradient(180deg,#8d8984 0%,#6e6a66 100%)}
.photo-barrow{background:
  radial-gradient(ellipse 90px 50px at 150px 50px,rgba(245,190,30,1) 0%,rgba(245,190,30,0) 100%),
  radial-gradient(ellipse 60px 35px at 110px 100px,rgba(90,90,90,.9) 0%,rgba(90,90,90,0) 100%),
  radial-gradient(ellipse 80px 40px at 40px 150px,rgba(200,150,60,.7) 0%,rgba(200,150,60,0) 100%),
  linear-gradient(180deg,#b8b1a6 0%,#9a9387 100%)}
.photo-blower{background:
  radial-gradient(ellipse 60px 60px at 140px 40px,rgba(40,170,90,1) 0%,rgba(40,170,90,0) 100%),
  radial-gradient(ellipse 90px 50px at 60px 150px,rgba(190,80,30,.95) 0%,rgba(190,80,30,0) 100%),
  radial-gradient(ellipse 80px 40px at 180px 160px,rgba(150,180,60,.9) 0%,rgba(150,180,60,0) 100%),
  radial-gradient(ellipse 70px 50px at 40px 40px,rgba(50,90,40,.95) 0%,rgba(50,90,40,0) 100%),
  linear-gradient(180deg,#4d7a35 0%,#7a9a3a 100%)}
.photo-rake{background:
  radial-gradient(ellipse 60px 40px at 60px 30px,rgba(50,60,70,.9) 0%,rgba(50,60,70,0) 100%),
  radial-gradient(ellipse 100px 50px at 120px 90px,rgba(230,150,30,.95) 0%,rgba(230,150,30,0) 100%),
  radial-gradient(ellipse 120px 40px at 120px 165px,rgba(70,150,40,1) 0%,rgba(70,150,40,0) 100%),
  linear-gradient(180deg,#6a5a3a 0%,#b07a28 55%,#4f8a2a 100%)}
.service-name{position:absolute;left:24px;top:203px;font-family:"Cinzel",Georgia,serif;font-weight:700;font-size:15px;color:var(--ink);white-space:nowrap}
.service-copy{position:absolute;left:22px;top:232px;width:205px;font-size:12px;line-height:23px;color:var(--text)}
.service-btn{position:absolute;left:22px;top:306px;width:101px;height:37px}

/* benefits */
.benefits-title{left:103px;top:1615px}
.benefit-list{left:114px;top:1672px;width:570px;list-style:none}
.benefit-list li{position:relative;padding-left:23px;font-size:12px;line-height:23px;margin-bottom:6px;color:var(--text)}
.benefit-list li svg{position:absolute;left:0;top:7px}
.benefit-list em{font-weight:700;color:var(--ink)}
.benefit-photo{left:700px;top:1627px;width:401px;height:311px;border:4px solid var(--white);box-shadow:0 0 0 1px #ccc;
  background:
    radial-gradient(ellipse 80px 140px at 150px 170px,rgba(240,235,225,.95) 0%,rgba(240,235,225,0) 100%),
    radial-gradient(ellipse 60px 80px at 330px 150px,rgba(200,200,205,.9) 0%,rgba(200,200,205,0) 100%),
    radial-gradient(ellipse 40px 60px at 60px 240px,rgba(190,40,40,.9) 0%,rgba(190,40,40,0) 100%),
    radial-gradient(ellipse 50px 150px at 270px 150px,rgba(90,55,40,.9) 0%,rgba(90,55,40,0) 100%),
    radial-gradient(ellipse 120px 80px at 60px 40px,rgba(140,170,90,.95) 0%,rgba(140,170,90,0) 100%),
    linear-gradient(180deg,#9aa872 0%,#7c6a55 60%,#5a4a3e 100%)}

/* footer */
.footer{left:0;top:1990px;width:1200px;height:244px;background:var(--footer)}
.footer-brand{left:100px;top:2062px;width:150px;text-align:center}
.footer-brand .brand-dot{background:#e6e6e6}
.footer-brand .brand-name{color:var(--white)}
.footer-divider{top:2030px;width:1px;height:170px;background:#4a4a4a}
.footer-heading{font-family:"Cinzel",Georgia,serif;font-size:19px;color:var(--white);letter-spacing:.5px}
.quick-links{left:375px;top:2068px;list-style:none}
.quick-links li{font-size:12px;line-height:22px;color:var(--footer-text);display:flex;align-items:center;gap:10px}
.contact-row{left:627px;display:flex;gap:14px;font-size:12px;line-height:18px;color:var(--footer-text)}
.news-copy{left:885px;top:2066px;width:220px;font-size:12px;line-height:19px;color:var(--footer-text)}
.news-input{left:885px;top:2118px;width:218px;height:31px;background:var(--white);border-radius:2px;font-size:11px;color:#aaa;padding:8px 12px}
.news-btn{left:885px;top:2162px;width:109px;height:37px}
.footer-bar{left:0;top:2234px;width:1200px;height:53px;background:var(--footer-bar)}
.copyright{left:99px;top:2252px;font-size:12px;color:var(--footer-text)}
.social{top:2241px;width:40px;height:40px;border-radius:50%;border:2px solid #ddd}
</style>
</head>
<body>

<!-- header -->
<div class="abs top-rule"></div>
<div class="abs brand"><span class="brand-dot"></span><span class="brand-name">MAPLE RIDGE</span></div>
<div class="abs header-phone">
  <svg width="16" height="16" viewBox="0 0 24 24"><path fill="#ec1f27" d="M6.6 10.8a15.1 15.1 0 0 0 6.6 6.6l2.2-2.2a1 1 0 0 1 1-.25 11.4 11.4 0 0 0 3.6.57 1 1 0 0 1 1 1V20a1 1 0 0 1-1 1A17 17 0 0 1 3 4a1 1 0 0 1 1-1h3.5a1 1 0 0 1 1 1c0 1.25.2 2.45.57 3.57a1 1 0 0 1-.25 1z"/></svg>
  (555) 214-3098
</div>
<nav class="main-nav">
  <a class="is-active" style="left:476px">HOME</a>
  <a style="left:563px">ABOUT</a>
  <a style="left:656px">SERVICES</a>
  <a style="left:766px">TESTIMONIALS</a>
  <a style="left:920px">BLOG</a>
  <a style="left:1000px">CONTACT US</a>
</nav>
<svg class="abs nav-underline" viewBox="0 0 68 6"><path d="M2 5 Q34 -2 66 5" stroke="#1b1b1b" stroke-width="2" fill="none"/></svg>

<!-- hero -->
<div class="abs hero" role="img" aria-label="Two-storey house with autumn trees and a leaf-covered front lawn"></div>
<div class="abs hero-shade"></div>
<svg class="abs hero-arrow" style="left:36px" width="16" height="40" viewBox="0 0 16 40"><path d="M14 2 L2 20 L14 38" stroke="#fff" stroke-width="2" fill="none"/></svg>
<svg class="abs hero-arrow" style="left:1148px" width="16" height="40" viewBox="0 0 16 40"><path d="M2 2 L14 20 L2 38" stroke="#fff" stroke-width="2" fill="none"/></svg>
<div class="abs hero-kicker">PRESERVE AND MAINTAIN THE VALUE</div>
<div class="abs hero-title">BEAUTY,SAFETY OF THEIR HOME</div>
<div class="abs btn hero-btn">View more</div>

<div class="abs appointment"></div>
<div class="abs appointment-head">Schedule an Appointment</div>
<div class="abs field field-select" style="top:265px">Reason for Inquiry (required)
  <svg width="10" height="6" viewBox="0 0 10 6"><path d="M1 1 L5 5 L9 1" stroke="#fff" stroke-width="1.5" fill="none"/></svg></div>
<div class="abs field" style="top:316px">Address</div>
<div class="abs field" style="top:368px">Email address</div>
<div class="abs field" style="top:419px">Phone number</div>
<div class="abs field field-area" style="top:468px">Description of Request</div>
<div class="abs btn send-btn">Send</div>

<!-- welcome -->
<div class="abs video-frame" role="img" aria-label="Gardener kneeling and planting in an autumn flower bed"></div>
<div class="abs play"><svg width="50" height="38" viewBox="0 0 50 38"><path d="M20 11 L32 19 L20 27 Z" fill="#fff"/></svg></div>
<h2 class="abs section-title welcome-title"><span class="title-dot"></span>WELCOME TO MAPLE RIDGE</h2>
<p class="abs welcome-copy">To deliver the proven Benefits of Preventive and Proactive maintainance to residential homeowners through a unique,comprehensive services package that is truly valued by our customers,makes their lives a little easier, and reduces the cost of home ownership.It is our goal to be viewed as trusted service partners operating solely in the best interst of our customers working together to preserve and maintain the value Beauty,safety of their home.We are committed to ensuring our services</p>
<div class="abs btn welcome-btn">View more info</div>

<!-- services -->
<div class="abs services"></div>
<h2 class="abs section-title services-title"><span class="title-dot"></span>OUR SERVICES</h2>
<div class="abs season-tab" style="left:99px;width:104px">Summer</div>
<div class="abs season-tab" style="left:209px;width:105px">Winter</div>
<div class="abs season-tab is-active" style="left:320px;width:105px">Fall</div>

<div class="abs service-card" style="left:99px">
  <div class="service-photo photo-sweep" role="img" aria-label="Broom sweeping fallen leaves on paving"></div>
  <div class="service-name">LEAVES RAKING</div>
  <p class="service-copy">It is our goal to be viewed as trusted service partners operating solely in the best interst of our customers</p>
  <div class="btn service-btn">View More</div>
</div>
<div class="abs service-card" style="left:354px">
  <div class="service-photo photo-barrow" role="img" aria-label="Wheelbarrow full of yellow leaves on cobblestones"></div>
  <div class="service-name">FALL | BUILD REALTY</div>
  <p class="service-copy">It is our goal to be viewed as trusted service partners operating solely in the best interst of our customers</p>
  <div class="btn service-btn">View More</div>
</div>
<div class="abs service-card" style="left:610px">
  <div class="service-photo photo-blower" role="img" aria-label="Leaf blower clearing leaves from a lawn"></div>
  <div class="service-name">POWERFUL LEAF BLOWER</div>
  <p class="service-copy">It is our goal to be viewed as trusted service partners operating solely in the best interst of our customers</p>
  <div class="btn service-btn">View More</div>
</div>
<div class="abs service-card" style="left:863px">
  <div class="service-photo photo-rake" role="img" aria-label="Rake gathering leaves on green grass"></div>
  <div class="service-name">CLEANING THE FALL</div>
  <p class="service-copy">It is our goal to be viewed as trusted service partners operating solely in the best interst of our customers</p>
  <div class="btn service-btn">View More</div>
</div>

<!-- benefits -->
<h2 class="abs section-title benefits-title"><span class="title-dot"></span>BENIFITS OF OUR CUSTOMERS</h2>
<ul class="abs benefit-list">
  <li><svg width="11" height="9" viewBox="0 0 11 9"><path d="M1 4.5 L4 7.5 L10 1" stroke="#1b1b1b" stroke-width="2" fill="none"/></svg><em>Extra time</em> to far too often very busy/damading lives.</li>
  <li><svg width="11" height="9" viewBox="0 0 11 9"><path d="M1 4.5 L4 7.5 L10 1" stroke="#1b1b1b" stroke-width="2" fill="none"/></svg><em>Savings</em> by performing on going maintainance and fixing-before-failure which Lowers the total cost of home ownership.</li>
  <li><svg width="11" height="9" viewBox="0 0 11 9"><path d="M1 4.5 L4 7.5 L10 1" stroke="#1b1b1b" stroke-width="2" fill="none"/></svg><em>Less work</em> and thing to do around the house.</li>
  <li><svg width="11" height="9" viewBox="0 0 11 9"><path d="M1 4.5 L4 7.5 L10 1" stroke="#1b1b1b" stroke-width="2" fill="none"/></svg><em>Stress reduction</em> with many fewer items opn to-do lists and additional time to spend on whatever fun/realaxing activities our customers.</li>
  <li><svg width="11" height="9" viewBox="0 0 11 9"><path d="M1 4.5 L4 7.5 L10 1" stroke="#1b1b1b" stroke-width="2" fill="none"/></svg><em>An answer</em> to the home maintenance faced by many who can no longer physically take care of their homes,providing yhe opportunity to 'age-in-place' as a viable option to down-sizing or retirement homes communities</li>
  <li><svg width="11" height="9" viewBox="0 0 11 9"><path d="M1 4.5 L4 7.5 L10 1" stroke="#1b1b1b" stroke-width="2" fill="none"/></svg><em>Peace of mind</em> knowing that &nbsp;their home is being professionally maintained as intended</li>
</ul>
<div class="abs benefit-photo" role="img" aria-label="Homeowner relaxing with a laptop on a sunny porch"></div>

<!-- footer -->
<div class="abs footer"></div>
<div class="abs footer-brand"><span class="brand-dot"></span><span class="brand-name">MAPLE RIDGE</span></div>
<div class="abs footer-divider" style="left:338px"></div>
<div class="abs footer-divider" style="left:595px"></div>
<div class="abs footer-divider" style="left:857px"></div>

<div class="abs footer-heading" style="left:375px;top:2028px">QUICK LINKS</div>
<ul class="abs quick-links">
  <li><svg width="5" height="8" viewBox="0 0 5 8"><path d="M1 1 L4 4 L1 7" stroke="#fff" fill="none"/></svg>Home</li>
  <li><svg width="5" height="8" viewBox="0 0 5 8"><path d="M1 1 L4 4 L1 7" stroke="#fff" fill="none"/></svg>About</li>
  <li><svg width="5" height="8" viewBox="0 0 5 8"><path d="M1 1 L4 4 L1 7" stroke="#fff" fill="none"/></svg>Services</li>
  <li><svg width="5" height="8" viewBox="0 0 5 8"><path d="M1 1 L4 4 L1 7" stroke="#fff" fill="none"/></svg>Testimonials</li>
  <li><svg width="5" height="8" viewBox="0 0 5 8"><path d="M1 1 L4 4 L1 7" stroke="#fff" fill="none"/></svg>Blog</li>
  <li><svg width="5" height="8" viewBox="0 0 5 8"><path d="M1 1 L4 4 L1 7" stroke="#fff" fill="none"/></svg>Contact Us</li>
</ul>

<div class="abs footer-heading" style="left:627px;top:2028px">CONTACT US</div>
<div class="abs contact-row" style="top:2068px">
  <svg width="12" height="16" viewBox="0 0 12 16"><path d="M6 0a6 6 0 0 0-6 6c0 4.5 6 10 6 10s6-5.5 6-10a6 6 0 0 0-6-6zm0 8.2A2.2 2.2 0 1 1 6 3.8a2.2 2.2 0 0 1 0 4.4z" fill="#fff"/></svg>
  <div>Yard Nest+<br>48 Cedar Hollow Rd.<br>Fairbrook, VA 20110</div>
</div>
<div class="abs contact-row" style="top:2145px">
  <svg width="14" height="14" viewBox="0 0 24 24"><path fill="#fff" d="M6.6 10.8a15.1 15.1 0 0 0 6.6 6.6l2.2-2.2a1 1 0 0 1 1-.25 11.4 11.4 0 0 0 3.6.57 1 1 0 0 1 1 1V20a1 1 0 0 1-1 1A17 17 0 0 1 3 4a1 1 0 0 1 1-1h3.5a1 1 0 0 1 1 1c0 1.25.2 2.45.57 3.57a1 1 0 0 1-.25 1z"/></svg>
  <div>(555) 214-3098</div>
</div>
<div class="abs contact-row" style="top:2193px">
  <svg width="16" height="14" viewBox="0 0 16 14"><rect x="0.5" y="3.5" width="15" height="10" rx="1" fill="none" stroke="#fff"/><rect x="3.5" y="0.5" width="9" height="4" fill="none" stroke="#fff"/><rect x="3" y="7" width="6" height="1.5" fill="#fff"/><rect x="3" y="10" width="6" height="1.5" fill="#fff"/></svg>
  <div>(555) 214-3099</div>
</div>

<div class="abs footer-heading" style="left:885px;top:2028px">NEWS LETTER</div>
<p class="abs news-copy">It is our goal to be viewed as trusted service partners operating</p>
<div class="abs news-input">Email address</div>
<div class="abs btn news-btn">Subcribe</div>

<div class="abs footer-bar"></div>
<div class="abs copyright">Copyright 2016 Maple Ridge. All Rights Reserved</div>
<div class="abs social" style="left:973px;background:#3b5998"></div>
<div class="abs social" style="left:1017px;background:#2ca7e0"></div>
<div class="abs social" style="left:1061px;background:#d6201f"></div>

</body>
</html>
```